Deactivated Coal-Fired Power Plant to be redeveloped into a Green Energy Campus.

Want a striking business card statement that introduces our concept project to provide economic and community recovery to a former rural coal community in western PA.
Essentially 12 project representatives that will lead both the demolition of an existing power plant and the redevelopment to a new Green energy site.
Business Card should reflect our effort.
We are open to ideas.

Target Market(s)

Energy and Power Generation industries

Industry/Entity Type

Power Generation and Data Centers

Contact Information for Business Card

Font styles to use
Sans Serif
Other font styles liked:
• Arial, Calibri

Requirements
Must have
• Multiple colors

```html
<!DOCTYPE html>
<html lang="en">
<head>
<meta charset="utf-8">
<title>Ridgeline Renewal — Business Card</title>
<link href="https://fonts.googleapis.com/css2?family=Roboto:wght@400;700;900&display=swap" rel="stylesheet">
<style>
  :root {
    --stage: #232323;
    --brand-green: #12984a;
    --brand-green-dark: #0d7a3b;
    --brand-green-light: #a9d870;
    --ink: #111111;
    --paper: #ffffff;
  }
  * { margin: 0; padding: 0; box-sizing: border-box; }
  html, body {
    width: 1200px; height: 780px; overflow: hidden;
    background: var(--stage);
    font-family: "Roboto", Arial, sans-serif;
  }
  .stage { position: relative; width: 1200px; height: 780px; }

  .card {
    position: absolute;
    width: 525px; height: 300px;
    box-shadow: 0 12px 30px rgba(0,0,0,.55);
    overflow: hidden;
  }

  /* Back of card */
  .card-back { left: 50px; top: 110px; background: var(--brand-green); }
  .card-back .pattern-fill {
    position: absolute; inset: 0;
    background: linear-gradient(200deg, var(--brand-green-light) 0%, var(--brand-green) 45%, var(--brand-green-dark) 100%);
    opacity: .9;
  }
  .card-back .wordmark {
    position: absolute; left: 50%; top: 50%;
    transform: translate(-50%, -50%);
    display: flex; align-items: center; gap: 12px;
  }
  .wordmark-dot {
    width: 46px; height: 46px; border-radius: 50%;
    background: var(--paper);
  }
  .card-back .wordmark-name {
    font-weight: 700; font-size: 30px; letter-spacing: .5px;
    color: var(--ink);
  }

  /* Front of card */
  .card-front { left: 625px; top: 370px; background: var(--paper); }
  .card-front .wordmark {
    position: absolute; right: 34px; top: 40px;
    display: flex; align-items: center; gap: 10px;
  }
  .card-front .wordmark-dot { background: var(--brand-green); width: 40px; height: 40px; }
  .card-front .wordmark-name { font-weight: 700; font-size: 24px; color: var(--ink); }

  .name-band {
    position: absolute; left: 0; top: 146px;
    width: 16px; height: 54px;
    background: var(--brand-green);
  }
  .identity { position: absolute; left: 34px; top: 140px; }
  .person-name { font-weight: 900; font-size: 30px; line-height: 1; }
  .person-name .first { color: var(--brand-green); }
  .person-name .last { color: var(--ink); }
  .person-title { font-size: 15px; color: var(--ink); margin-top: 4px; }
  .company { font-size: 15px; color: var(--brand-green); margin-top: 12px; }

  .contacts { position: absolute; left: 40px; top: 226px; list-style: none; }
  .contacts li {
    display: flex; align-items: center; gap: 8px;
    font-size: 13.5px; color: var(--ink); line-height: 20px;
  }
  .contacts svg { width: 14px; height: 14px; flex: none; }
</style>
</head>
<body>
<main class="stage">

  <section class="card card-back" aria-label="Business card back">
    <div class="pattern-fill" role="img" aria-label="Repeating pattern of the company symbol over green"></div>
    <div class="wordmark">
      <span class="wordmark-dot"></span>
      <span class="wordmark-name">Ridgeline Renewal</span>
    </div>
  </section>

  <section class="card card-front" aria-label="Business card front">
    <div class="wordmark">
      <span class="wordmark-dot"></span>
      <span class="wordmark-name">Ridgeline Renewal</span>
    </div>

    <div class="name-band"></div>
    <div class="identity">
      <h1 class="person-name"><span class="first">Daniel</span> <span class="last">Whitford</span></h1>
      <p class="person-title">Chief Operating Officer</p>
      <p class="company">Ridgeline Renewal LLC</p>
    </div>

    <ul class="contacts">
      <li>
        <svg viewBox="0 0 14 14" aria-hidden="true"><rect x="3.5" y="1" width="7" height="12" rx="1.5" fill="none" stroke="#12984a" stroke-width="1.3"/><circle cx="7" cy="11" r=".7" fill="#12984a"/></svg>
        555.014.2200
      </li>
      <li>
        <svg viewBox="0 0 14 14" aria-hidden="true"><circle cx="7" cy="7" r="5.8" fill="none" stroke="#12984a" stroke-width="1.3"/><path d="M1.2 7h11.6M7 1.2c-2.4 3-2.4 8.6 0 11.6M7 1.2c2.4 3 2.4 8.6 0 11.6" fill="none" stroke="#12984a" stroke-width="1"/></svg>
        www.ridgelinerenewal.com
      </li>
      <li>
        <svg viewBox="0 0 14 14" aria-hidden="true"><rect x="1" y="3" width="12" height="8.5" fill="none" stroke="#12984a" stroke-width="1.3"/><path d="M1 3l6 5 6-5" fill="none" stroke="#12984a" stroke-width="1.2"/></svg>
        dwhitford@ridgelinerenewal.com
      </li>
    </ul>
  </section>

</main>
</body>
</html>
```